RW Skyline Imaging Web Site design

I am looking for a responsive single page website deign for rwskylineimages.example. This is a drone based aerial photography and cinematography business. It should have an about us section, a services section that contains photograph service, Video footage, and Aerial mapping all under the services section, a pricing section, and then a contact page for customers to contact us.

Coding

Coded - Design and coding required

Number of Pages Required

1 page

Font styles to use
Sans Serif

Colors

Designer to choose colors to be used in the design.

Requirements
Must have
• Responsive design. About us section, services section, pricing section under the services links, and contact us section, that links to a submission page where they can send Name, address, email, and comments on what they are interested in.
• See flyquad7x.example - looking for similar design.
Should not have
• clutter, or too busy design

```html
<!DOCTYPE html>
<html lang="en">
<head>
<meta charset="utf-8">
<title>RW Skyline Imaging – Aerial Photography</title>
<link rel="stylesheet" href="https://fonts.googleapis.com/css2?family=Montserrat:wght@400;500;600;700&family=Open+Sans:wght@400;600&display=swap">
<style>
:root{
  --orange:#f7901e;
  --dark:#2b2b2b;
  --ink:#222222;
  --text:#555555;
  --muted:#8a8a8a;
  --grey-band:#e6e6e6;
  --footer:#2d2d2d;
  --footer-text:#cfcfcf;
  --white:#ffffff;
}
*{box-sizing:border-box;margin:0;padding:0}
html,body{width:1200px;height:4455px;overflow:hidden}
body{position:relative;background:var(--white);font-family:"Open Sans",Arial,sans-serif;color:var(--text)}
.abs{position:absolute}
h1,h2,h3,.nav a,.btn{font-family:"Montserrat",Arial,sans-serif}

/* header */
.site-header{left:0;top:0;width:1200px;height:119px;background:var(--white)}
.brand{left:88px;top:38px;display:flex;align-items:center;gap:12px}
.brand-mark{width:22px;height:22px;background:var(--orange)}
.brand-name{font-family:"Montserrat",sans-serif;font-size:19px;font-weight:500;letter-spacing:2px;color:var(--ink)}
.nav{right:82px;top:70px;display:flex;gap:34px}
.nav a{font-size:13px;text-decoration:none;color:#444;letter-spacing:.5px}
.nav a.active{color:var(--ink);border-bottom:2px solid var(--orange);padding-bottom:6px}

/* hero */
.hero{left:0;top:119px;width:1200px;height:638px;background:linear-gradient(180deg,#b9cfdc 0%,#7ea3b8 30%,#4f8197 55%,#2e6b7c 75%,#1f5563 100%)}
.hero-cut{left:0;top:119px}
.hero-title{left:0;top:278px;width:1200px;text-align:center;color:var(--white);font-size:34px;font-weight:700}
.hero-sub{left:0;top:335px;width:1200px;text-align:center;color:var(--white);font-family:"Montserrat",sans-serif;font-size:26px;font-weight:400;letter-spacing:.5px}
.btn{display:block;background:var(--orange);color:var(--white);text-align:center;text-decoration:none}
.hero-btn{left:467px;top:401px;width:211px;height:51px;line-height:51px;font-size:17px}

/* intro */
.section-title{color:var(--ink);font-weight:500;letter-spacing:1px}
.intro-title{left:85px;top:880px;font-size:34px}
.intro-text{left:85px;top:946px;width:440px;font-size:12.5px;line-height:20px}
.intro-text p+p{margin-top:14px}
.video{left:564px;top:864px;width:550px;height:321px;background:linear-gradient(135deg,#c9b79a 0%,#8fa7a8 40%,#3f7e8f 70%,#2b6272 100%)}

/* recent work */
.orange-band{left:0;top:1328px;width:1200px;height:493px;background:var(--orange)}
.camera{left:60px;top:1283px;width:320px;height:416px;background:linear-gradient(180deg,#3a3a3a,#1c1c1c);border-radius:10px}
.recent-title{left:500px;top:1378px;width:555px;display:flex;align-items:center;gap:18px;color:var(--white);font-size:34px;font-weight:500;letter-spacing:1px}
.recent-title .rule{flex:1;height:2px;background:var(--white)}
.slider{left:499px;top:1452px;width:552px;height:321px;background:linear-gradient(135deg,#b7b4a6 0%,#9c7f6a 35%,#8aa39a 60%,#5f8079 100%)}

/* services */
.services-title{left:0;top:1896px;width:1200px;text-align:center;font-size:34px}
.service-card{top:2011px;width:252px;height:336px}
.service-card.featured{border:1px solid #dcdcdc}
.service-icon{position:absolute;left:67px;top:38px;width:118px;height:118px;border-radius:50%;background:var(--dark);display:flex;align-items:center;justify-content:center}
.featured .service-icon{background:var(--orange)}
.service-text{position:absolute;left:22px;top:184px;width:208px;text-align:center;font-size:12px;line-height:19px;color:#444}

/* work grid */
.work-title{left:0;top:2490px;width:1200px;text-align:center;font-size:34px}
.work-grid{left:0;top:2593px;width:1200px;display:grid;grid-template-columns:repeat(4,300px);grid-auto-rows:226px;gap:0}

/* pilots */
.pilots-band{left:0;top:3231px}
.pilots-title{left:0;top:3312px;width:1200px;text-align:center;font-size:34px}
.pilot{top:3418px;width:240px;text-align:center}
.pilot-photo{width:184px;height:184px;margin:0 auto;border-radius:50%;border:6px solid var(--orange)}
.pilot-name{margin-top:36px;font-family:"Montserrat",sans-serif;font-size:20px;font-weight:600;color:#333;letter-spacing:.5px}
.pilot-bio{margin-top:12px;font-size:13.5px;line-height:19px;color:#666}

/* footer */
.site-footer{left:0;top:3837px;width:1200px;height:618px;background:var(--footer)}
.social{left:510px;top:3902px;display:flex;gap:22px}
.social span{width:40px;height:40px;border-radius:50%;border:1px solid #555;display:block}
.social span.on{background:var(--orange);border-color:var(--orange)}
.contact-form{left:104px;top:3992px;width:276px}
.field{width:276px;height:31px;background:var(--white);margin-bottom:9px;font-size:11px;color:#999;padding:8px 10px;line-height:15px}
.field.area{height:78px}
.submit{width:113px;height:36px;line-height:36px;font-size:14px;font-weight:600;margin-top:17px}
.footer-head{left:463px;top:3990px;font-family:"Montserrat",sans-serif;font-size:14px;font-weight:600;color:var(--white);letter-spacing:1px}
.col-title{font-family:"Montserrat",sans-serif;font-size:13px;font-weight:600;color:var(--white);letter-spacing:1px;margin-bottom:12px}
.col{top:4025px;font-size:12px;color:var(--footer-text)}
.addr-row{display:flex;gap:12px;margin-bottom:16px;line-height:16px}
.addr-row svg{flex:none;margin-top:1px}
.list{list-style:none}
.list li{margin-bottom:13px;padding-left:16px;position:relative}
.list li::before{content:"";position:absolute;left:0;top:6px;width:5px;height:5px;border-radius:50%;background:var(--footer-text)}
.footer-note{left:120px;top:4322px;width:960px;text-align:center;font-size:12.5px;line-height:21px;color:var(--footer-text)}
</style>
</head>
<body>

<header class="abs site-header">
  <div class="abs brand"><span class="brand-mark"></span><span class="brand-name">RW Skyline Imaging</span></div>
  <nav class="abs nav">
    <a class="active" href="#home">HOME</a>
    <a href="#about">ABOUT US</a>
    <a href="#services">SERVICES</a>
    <a href="#video-footage">VIDEO FOOTAGE</a>
    <a href="#pricing">PRICING</a>
    <a href="#contact">CONTACTS</a>
  </nav>
</header>

<section id="home">
  <div class="abs hero" role="img" aria-label="Drone with camera hovering above a coastal bay and green hills"></div>
  <svg class="abs hero-cut" width="1200" height="640" viewBox="0 0 1200 640">
    <polygon points="0,519 280,638 1200,471 1200,640 0,640" fill="#ffffff"/>
  </svg>
  <h1 class="abs hero-title">Aerial Photography for Real Estate Architectural Sports</h1>
  <p class="abs hero-sub">Commercial Advertising &amp; Enviromental Professionals</p>
  <a class="abs btn hero-btn" href="#about">Learn More</a>
</section>

<section id="about">
  <h2 class="abs section-title intro-title">INTRODUCTION</h2>
  <div class="abs intro-text">
    <p>We fly licensed drones over homes, venues and job sites to capture the views you can't get from the ground. Every flight is planned, insured and shot in high resolution so your project looks its best from above.</p>
    <p>From a single listing to a full build season, we deliver clean stills and smooth footage on time.</p>
  </div>
  <div class="abs video" role="img" aria-label="Aerial video of a beachfront neighbourhood and ocean">
    <svg width="550" height="321" viewBox="0 0 550 321">
      <circle cx="275" cy="155" r="32" fill="rgba(0,0,0,.55)"/>
      <polygon points="266,140 266,170 291,155" fill="#fff"/>
      <rect x="0" y="277" width="550" height="44" fill="rgba(0,0,0,.6)"/>
      <polygon points="34,290 34,308 48,299" fill="#fff"/>
      <rect x="82" y="296" width="300" height="5" fill="rgba(255,255,255,.35)"/>
      <rect x="395" y="292" width="30" height="12" fill="#fff" opacity=".7"/>
      <rect x="514" y="16" width="24" height="24" rx="3" fill="rgba(0,0,0,.55)"/>
      <rect x="514" y="46" width="24" height="24" rx="3" fill="rgba(0,0,0,.55)"/>
    </svg>
  </div>
</section>

<section class="recent-work">
  <div class="abs orange-band"></div>
  <div class="abs camera" role="img" aria-label="Drone gimbal camera product shot"></div>
  <h2 class="abs recent-title"><span class="rule"></span>RECENT WORK<span class="rule"></span></h2>
  <div class="abs slider" role="img" aria-label="Aerial view of red-roofed buildings and city towers">
    <svg width="552" height="321" viewBox="0 0 552 321">
      <rect x="0" y="130" width="22" height="56" fill="rgba(0,0,0,.45)"/>
      <polyline points="14,148 8,158 14,168" fill="none" stroke="#fff" stroke-width="2"/>
      <rect x="530" y="130" width="22" height="56" fill="rgba(0,0,0,.45)"/>
      <polyline points="538,148 544,158 538,168" fill="none" stroke="#fff" stroke-width="2"/>
    </svg>
  </div>
</section>

<section id="services">
  <h2 class="abs section-title services-title">OUR SERVICES</h2>

  <div id="photograph-service" class="abs service-card" style="left:73px">
    <div class="service-icon"><svg width="36" height="28" viewBox="0 0 36 28" fill="none" stroke="#fff" stroke-width="2"><rect x="2" y="6" width="32" height="20" rx="3"/><path d="M12 6l3-4h6l3 4"/><circle cx="18" cy="16" r="6"/></svg></div>
    <p class="service-text">Photograph service: sharp, high resolution aerial stills of homes, buildings, venues and events, edited and colour corrected so every listing or project shows its best side from above.</p>
  </div>

  <div id="video-footage" class="abs service-card featured" style="left:342px">
    <div class="service-icon"><svg width="38" height="26" viewBox="0 0 38 26" fill="none" stroke="#fff" stroke-width="2"><rect x="2" y="5" width="24" height="18" rx="2"/><path d="M26 11l10-6v16l-10-6"/><circle cx="9" cy="11" r="2"/></svg></div>
    <p class="service-text">Video footage: smooth 4K cinematic flyovers that tell the story of your property, company or event, delivered as a finished edit with music or as raw clips.</p>
  </div>

  <div id="aerial-mapping" class="abs service-card" style="left:619px">
    <div class="service-icon"><svg width="34" height="34" viewBox="0 0 34 34" fill="none" stroke="#fff" stroke-width="2" stroke-linejoin="round"><polygon points="17,3 21,13 32,13 23,20 26,31 17,24 8,31 11,20 2,13 13,13"/></svg></div>
    <p class="service-text">Aerial mapping: accurate orthomosaic maps and site surveys for builders, farms and environmental teams, so you can measure, plan and track progress with ease.</p>
  </div>

  <div id="pricing" class="abs service-card" style="left:881px">
    <div class="service-icon"><svg width="38" height="30" viewBox="0 0 38 30" fill="none" stroke="#fff" stroke-width="2" stroke-linejoin="round"><polygon points="19,3 36,11 19,19 2,11"/><path d="M9 15v8c5 5 15 5 20 0v-8"/><path d="M34 12v9"/></svg></div>
    <p class="service-text">Pricing: photo packages from $199, video footage from $349, aerial mapping quoted per acre. Flat rates, no hidden fees, travel included within 40 miles.</p>
  </div>
</section>

<section class="work">
  <h2 class="abs section-title work-title">WORK</h2>
  <div class="abs work-grid">
    <div role="img" aria-label="Person in a canoe on a forest lake" style="background:linear-gradient(160deg,#1d3a3f,#2f6a78 60%,#1a3b45)"></div>
    <div role="img" aria-label="Bride holding a bouquet" style="background:linear-gradient(160deg,#cdd0d2,#e8e6e2 55%,#9aa4a2)"></div>
    <div role="img" aria-label="Road leading to snowy mountains" style="background:linear-gradient(180deg,#6f8eb5,#b8c4cf 45%,#5b5c58 80%)"></div>
    <div role="img" aria-label="Portrait of a man in a hat and dark coat" style="background:linear-gradient(160deg,#5a5e60,#2e3032 60%,#1c1d1e)"></div>
    <div role="img" aria-label="Plate of cookies on a dark table" style="background:linear-gradient(160deg,#253038,#8a5a2a 55%,#2a3339)"></div>
    <div role="img" aria-label="Suspension bridge at sunset" style="background:linear-gradient(180deg,#e29a63,#c7683e 50%,#3c5360)"></div>
    <div role="img" aria-label="Green plant and bowl on a dark table" style="background:linear-gradient(160deg,#1f2422,#3f5a3a 50%,#2a2d2b)"></div>
    <div role="img" aria-label="Fashion portrait of a woman in white" style="background:linear-gradient(160deg,#a8b3a5,#5d4a3e 55%,#c9cbc6)"></div>
  </div>
</section>

<section id="pilots">
  <svg class="abs pilots-band" width="1200" height="606" viewBox="0 0 1200 606">
    <polygon points="0,140 505,0 1200,140 1200,606 0,606" fill="#e6e6e6"/>
  </svg>
  <h2 class="abs section-title pilots-title">DRONE PILOTS</h2>
  <div class="abs pilot" style="left:79px"><div class="pilot-photo" role="img" aria-label="Pilot portrait" style="background:linear-gradient(160deg,#8aa0ae,#4c5862)"></div><p class="pilot-name">PILOT: JHON DOE</p><p class="pilot-bio">I'm a paragraph. Click here to add your own text and edit me. Let your users get to know you.</p></div>
  <div class="abs pilot" style="left:349px"><div class="pilot-photo" role="img" aria-label="Pilot portrait" style="background:linear-gradient(160deg,#b9c2c6,#2d2f33)"></div><p class="pilot-name">PILOT: JHON DOE</p><p class="pilot-bio">I'm a paragraph. Click here to add your own text and edit me. Let your users get to know you.</p></div>
  <div class="abs pilot" style="left:617px"><div class="pilot-photo" role="img" aria-label="Pilot portrait" style="background:linear-gradient(160deg,#c9a27a,#7a3b3b)"></div><p class="pilot-name">PILOT: JHON DOE</p><p class="pilot-bio">I'm a paragraph. Click here to add your own text and edit me. Let your users get to know you.</p></div>
  <div class="abs pilot" style="left:881px"><div class="pilot-photo" role="img" aria-label="Pilot portrait" style="background:linear-gradient(160deg,#d7d2c8,#3a3d44)"></div><p class="pilot-name">PILOT: JHON DOE</p><p class="pilot-bio">I'm a paragraph. Click here to add your own text and edit me. Let your users get to know you.</p></div>
</section>

<footer id="contact" class="abs site-footer"></footer>
<div class="abs social"><span></span><span class="on"></span><span></span><span></span><span></span></div>

<form class="abs contact-form">
  <div class="field">Your Name</div>
  <div class="field">Your Email</div>
  <div class="field">Your Address</div>
  <div class="field area">Your comments</div>
  <div class="btn submit">SUBMIT</div>
</form>

<p class="abs footer-head">PHOTOGRAPHS RW SKYLINE IMAGING</p>

<div class="abs col" style="left:463px;width:220px">
  <p class="col-title">ADDRESS</p>
  <div class="addr-row"><svg width="14" height="18" viewBox="0 0 14 18"><path d="M7 1a6 6 0 0 0-6 6c0 4 6 10 6 10s6-6 6-10a6 6 0 0 0-6-6z" fill="#fff"/><circle cx="7" cy="7" r="2" fill="#2d2d2d"/></svg><span>240 Harbor View Lane<br>Dummy Address,<br>CA 94158</span></div>
  <div class="addr-row"><svg width="16" height="16" viewBox="0 0 16 16" fill="none" stroke="#fff" stroke-width="1.4"><circle cx="8" cy="8" r="7"/><ellipse cx="8" cy="8" rx="3" ry="7"/><path d="M1 8h14"/></svg><span>rwskylineimages.example</span></div>
  <div class="addr-row" style="margin-top:22px"><svg width="16" height="16" viewBox="0 0 16 16"><path d="M3 1l3 3-2 2c1 2 3 4 5 5l2-2 3 3-2 3C7 15 1 9 1 3z" fill="#fff"/></svg><span>555-0142</span></div>
  <div class="addr-row" style="margin-top:22px"><svg width="16" height="12" viewBox="0 0 16 12"><rect x="0" y="0" width="16" height="12" fill="#fff"/><polyline points="0,0 8,7 16,0" fill="none" stroke="#2d2d2d" stroke-width="1.4"/></svg><span>hi@rwskylineimages.example</span></div>
</div>

<div class="abs col" style="left:713px">
  <p class="col-title">LINKS</p>
  <ul class="list"><li>Home</li><li>About Us</li><li>Services</li><li>Video Footage</li><li>Pricing</li><li>Contacts</li></ul>
</div>

<div class="abs col" style="left:888px">
  <p class="col-title">SERVICES</p>
  <ul class="list"><li>Contains Photograph Service</li><li>Video Footage</li><li>Aerial mapping</li></ul>
</div>

<p class="abs footer-note">Riley Wardell Aerial Photography provides services for Real Estate, Architectural, Sports Commercial, Advertising, Environmental professionals or personal aerial photo sessions. We serve San Diego South Riverside Orange and Los Angeles counties with the best aerial photography around. All photographs are copyright protected and the property of Riley Wardell Aerial Photography</p>

</body>
</html>
```